Yoghurt drink 300 ml bottle for Australian Market

I need to design the artwork for shrink sleeve label of a 300 ml plastic bottle, the design will show the brand name "Kelvra" with the description "active yoghurt drink ", it will have the usual information fields such as ingredient, nutrition facts, barcode in addition to a field for "health benefits ".

The colour scheme will be one of two choices, green and navy (with white).

The word "Kelvra" will have simple clipart type drawing of "snow mountains " at its background ( just around the word, not covering the whole label)

At the top of the label the words "Refresh, rejuvenate!!" will be placed suitably near the neck of the bottle.

The shrink label is to cover the whole bottle from neck to bottom.

Attached 2 pictures for similar designs to give you an ideas (do not restrict your creativity)

The bottle photo attached, bottle dimension are:
Height: (up to bottle neck) 125 mm
Base parameter: 62 mm

Let me know if you need further details
Updates

Target Market(s)

Youth, healthy food customers, athletic people, normal customers.

Industry/Entity Type

Retail

Font styles to use
Sans Serif

Requirements
Must have
• The bottle looks original and stands out.
• The only bottle cap available to me is in blue color as in attached picture, please incorporate this color into your design, maybe the logo.
• Information on the label:
• Ingredients: Milk, Milk solids, water, cultures.
• Nutrition information:
• Serving per bottle: 1 Serving size 300 ml
• Quantity per serving Quantity per 100g
• Energy. 576kJ 192kJ
• Protein. 7.5g. 2.5g
• Fat, total. 8.4g 2.8g
• Saturated. 5.4g. 1.8g
• Carbohydrate 9.3g 3.1g
• Sugars 9.3g 3.1g
• Sodium 276mg. 92mg
• Calcium. 480mg. 160mg
• Storage: store at or below 5 C
• Shake well before opening.
• Best before: see date print on the bottle.
• Made in Australia
• By Denmor Palikue Pty Ltd
• 7/4 Tunmore Road
• Henlow WA 6142
• 08 93158207
• Info@kelvra.com.au
• Barcode information:
• GTIN : 9312847065823 (other files and info available upon request)

```html
<!DOCTYPE html>
<html lang="en">
<head>
<meta charset="utf-8">
<title>Kelvra Active Yoghurt Drink – 300 ml sleeve</title>
<link rel="stylesheet" href="https://fonts.googleapis.com/css2?family=Kaushan+Script&family=Oswald:wght@400;600&display=swap">
<style>
  :root {
    --bg: #ffffff;
    --cap-blue: #1f4fb8;
    --cap-blue-dark: #163c8f;
    --green-deep: #0b4418;
    --green-mid: #17672a;
    --green-glow: #6aa72c;
    --milk: #ffffff;
    --milk-shade: #e4e8e6;
    --label-white: #ffffff;
    --volume-green: #14512a;
  }
  html, body {
    margin: 0;
    padding: 0;
    width: 1200px;
    height: 1200px;
    overflow: hidden;
    background: var(--bg);
  }
  .sleeve-sheet {
    display: block;
    width: 1200px;
    height: 1200px;
  }
  .tagline {
    font-family: "Kaushan Script", cursive;
    font-size: 27px;
    fill: var(--label-white);
  }
  .brand-name {
    font-family: "Oswald", sans-serif;
    font-weight: 600;
    font-size: 104px;
    letter-spacing: 2px;
    fill: var(--label-white);
  }
  .product-line {
    font-family: "Oswald", sans-serif;
    font-weight: 400;
    font-size: 34px;
    fill: var(--label-white);
  }
  .volume {
    font-family: "Oswald", sans-serif;
    font-weight: 400;
    font-size: 34px;
    fill: var(--volume-green);
  }
  .cap-body { fill: var(--cap-blue); }
  .cap-ridge { stroke: var(--cap-blue-dark); stroke-width: 2; }
  .cap-band { fill: var(--cap-blue-dark); }
</style>
</head>
<body>
<svg class="sleeve-sheet" viewBox="0 0 1200 1200" xmlns="http://www.w3.org/2000/svg">
  <defs>
    <radialGradient id="sleeve-green" cx="0.5" cy="0.38" r="0.62">
      <stop offset="0" stop-color="#6aa72c"/>
      <stop offset="0.45" stop-color="#17672a"/>
      <stop offset="1" stop-color="#0b4418"/>
    </radialGradient>
    <linearGradient id="milk-fill" x1="0" y1="0" x2="0" y2="1">
      <stop offset="0" stop-color="#ffffff"/>
      <stop offset="1" stop-color="#e4e8e6"/>
    </linearGradient>
    <clipPath id="sleeve-outline">
      <path d="M270,272 L518,272 C520,300 505,312 502,332 C498,362 560,392 570,462 L576,1000 C576,1080 560,1110 520,1118 L268,1118 C228,1110 212,1080 212,1000 L218,462 C228,392 290,362 286,332 C283,312 268,300 270,272 Z"/>
    </clipPath>
  </defs>

  <g class="bottle bottle-left">
    <g class="sleeve" clip-path="url(#sleeve-outline)">
      <rect class="sleeve-ground" x="200" y="260" width="390" height="870" fill="url(#sleeve-green)"/>
      <path role="img" aria-label="Milk splash rising across the lower part of the sleeve" d="M200,860 C240,820 260,800 290,830 C330,870 370,900 420,880 C460,860 470,830 500,840 C530,850 540,820 560,800 L590,790 L590,1130 L200,1130 Z" fill="url(#milk-fill)"/>
    </g>
    <text class="tagline" x="394" y="385" text-anchor="middle" textLength="250" lengthAdjust="spacingAndGlyphs">Refresh, rejuvenate!!</text>
    <text class="brand-name" x="394" y="682" text-anchor="middle">Kelvra</text>
    <text class="product-line" x="394" y="738" text-anchor="middle">ACTIVE YOGHURT</text>
    <text class="product-line" x="394" y="774" text-anchor="middle">DRINK</text>
    <text class="volume" x="394" y="1070" text-anchor="middle">300 ML</text>
    <g class="cap">
      <rect class="cap-body" x="266" y="180" width="262" height="94" rx="10"/>
      <rect class="cap-band" x="266" y="250" width="262" height="22" rx="4"/>
      <path class="cap-ridge" d="M290,188V248M314,186V248M338,186V248M362,186V248M386,186V248M410,186V248M434,186V248M458,186V248M482,186V248M506,188V248"/>
    </g>
  </g>

  <g class="bottle bottle-right" transform="translate(430 0)">
    <g class="sleeve" clip-path="url(#sleeve-outline)">
      <rect class="sleeve-ground" x="200" y="260" width="390" height="870" fill="url(#sleeve-green)"/>
      <path role="img" aria-label="Milk splash rising across the lower part of the sleeve" d="M200,860 C240,820 260,800 290,830 C330,870 370,900 420,880 C460,860 470,830 500,840 C530,850 540,820 560,800 L590,790 L590,1130 L200,1130 Z" fill="url(#milk-fill)"/>
    </g>
    <text class="tagline" x="394" y="385" text-anchor="middle" textLength="250" lengthAdjust="spacingAndGlyphs">Refresh, rejuvenate!!</text>
    <text class="brand-name" x="394" y="682" text-anchor="middle">Kelvra</text>
    <text class="product-line" x="394" y="738" text-anchor="middle">ACTIVE YOGHURT</text>
    <text class="product-line" x="394" y="774" text-anchor="middle">DRINK</text>
    <text class="volume" x="394" y="1070" text-anchor="middle">300 ML</text>
    <g class="cap">
      <rect class="cap-body" x="266" y="180" width="262" height="94" rx="10"/>
      <rect class="cap-band" x="266" y="250" width="262" height="22" rx="4"/>
      <path class="cap-ridge" d="M290,188V248M314,186V248M338,186V248M362,186V248M386,186V248M410,186V248M434,186V248M458,186V248M482,186V248M506,188V248"/>
    </g>
  </g>
</svg>
</body>
</html>
```